Velmorra, a Pet Sanitizer using a non alcohol product

It's a label for a Pet Sanitizer. I have attached my proposed concept.
It's going to be on a 500 mil plastic spray bottle. What I did is my idea I want to see yours. In the end, I want two versions, one label for a white spray bottle and one for a cobalt blue bottle The seal I used is only an example. I need it to stand out and transparent to the background.
The label needs to look safe, professional, current, and friendly.
My label looks a bit busy, dark, and not professional. please give me your ideas and concept. Thx,
Updates

"Velmorra" is the company name. I have attached the company's logo herein. However, I believe that in today's market the logos are not important. Maybe you can make the water drop a watermark behind the company name. This is only a suggestion and I will wait to see your ideas. Thx,

Target Market(s)

Pet Owners

Industry/Entity Type

Pet Care

Font styles to use
Sans Serif

Requirements
Must have
• see upload file
Nice to have
• Professional
Should not have
• cartoons

```html
<!DOCTYPE html>
<html lang="en">
<head>
<meta charset="UTF-8">
<title>Velmorra Antimicrobial Pet Sanitizer Label</title>
<link href="https://fonts.googleapis.com/css2?family=Oswald:wght@500;600&family=Montserrat:wght@400;500;600&display=swap" rel="stylesheet">
<style>
  :root{
    --navy:#0f1b3d;
    --navy-soft:#2a3552;
    --ink:#1d2a4d;
    --slate:#4a5677;
    --sky:#3fa9dc;
    --sky-deep:#1b7fc0;
    --sky-light:#6cc3ea;
    --paper:#ffffff;
    --page:#f4f6f9;
    --line:#8a8f99;
    --seal:#7dbb7a;
    --icon:#6b7280;
  }
  *{box-sizing:border-box;margin:0;padding:0}
  html,body{width:1200px;height:1200px;overflow:hidden;background:var(--page)}
  .canvas{position:relative;width:1200px;height:1200px}
  .label{
    position:absolute;left:170px;top:50px;width:860px;height:1100px;
    background:var(--paper);overflow:hidden;
    box-shadow:0 8px 30px rgba(15,27,61,.12);
    font-family:"Montserrat",sans-serif;
  }
  .brand-band{
    position:absolute;left:0;top:0;width:100%;height:185px;
    background:linear-gradient(90deg,var(--navy-soft) 0%,var(--navy) 50%,var(--navy-soft) 100%);
    display:flex;align-items:center;justify-content:center;gap:18px;
  }
  .brand-dot{width:22px;height:22px;border-radius:50%;border:3px solid #fff}
  .brand-name{color:#fff;font-family:"Montserrat",sans-serif;font-weight:500;font-size:46px;letter-spacing:12px}
  .origin-badge{
    position:absolute;left:500px;top:150px;width:122px;height:122px;border-radius:50%;
    background:#fff;border:4px solid var(--navy);box-shadow:0 0 0 6px #fff,0 0 0 8px #c7ccd6;
  }
  .claims{position:absolute;top:290px;left:0;width:100%;display:flex;justify-content:center;gap:18px}
  .claim{
    width:86px;height:86px;border-radius:50%;border:2px dashed var(--icon);
    display:flex;align-items:center;justify-content:center;text-align:center;
    font-size:11px;font-weight:600;color:var(--slate);line-height:1.15;letter-spacing:.5px
  }
  .title{position:absolute;top:435px;left:0;width:100%;text-align:center;font-family:"Oswald",sans-serif;font-weight:600;line-height:1}
  .title-top{font-size:96px;color:var(--sky);letter-spacing:1px}
  .title-top span{color:var(--sky-deep)}
  .title-bottom{font-size:96px;color:var(--ink);margin-top:6px}
  .title-bottom span{color:var(--slate);font-weight:500}
  .tagline{
    position:absolute;top:665px;left:120px;width:620px;height:50px;
    background:linear-gradient(90deg,rgba(63,169,220,0) 0%,rgba(63,169,220,.35) 50%,rgba(63,169,220,0) 100%);
    display:flex;align-items:center;justify-content:center;
    font-size:30px;color:var(--slate);font-weight:500;white-space:nowrap
  }
  .tagline b{color:var(--ink);font-weight:600}
  .efficacy{position:absolute;top:745px;left:180px;width:460px;text-align:center;font-size:31px;color:var(--ink);font-weight:500;line-height:1.35}
  .rule{position:absolute;top:852px;left:205px;width:430px;height:3px;background:var(--line)}
  .benefits{position:absolute;top:870px;left:180px;width:460px;text-align:center;font-size:31px;color:var(--sky);font-weight:500}
  .pet-seal{
    position:absolute;left:632px;top:755px;width:146px;height:146px;border-radius:50%;
    border:4px solid var(--seal);opacity:.75;background:rgba(125,187,122,.08)
  }
  .species{
    position:absolute;left:178px;top:935px;width:500px;height:78px;
    background:linear-gradient(90deg,var(--navy-soft),var(--slate));border-radius:10px;opacity:.85
  }
  .volume-band{
    position:absolute;left:0;top:1025px;width:100%;height:75px;
    background:linear-gradient(90deg,var(--sky-light),var(--sky-deep));
    border-top:12px solid var(--sky-light);
    display:flex;align-items:center;justify-content:center;
    color:#fff;font-size:34px;font-weight:500;letter-spacing:1px
  }
</style>
</head>
<body>
<div class="canvas">
  <div class="label">
    <div class="brand-band">
      <span class="brand-dot"></span>
      <span class="brand-name">VELMORRA</span>
    </div>
    <div class="origin-badge" role="img" aria-label="Made in USA badge"></div>

    <div class="claims">
      <div class="claim">NON<br>TOXIC</div>
      <div class="claim">ALCOHOL<br>FREE</div>
      <div class="claim">NATURAL<br>PURE</div>
      <div class="claim">HYPO-<br>ALLERGENIC</div>
      <div class="claim">NON-<br>SCENTED</div>
      <div class="claim">VEGAN</div>
    </div>

    <div class="title">
      <div class="title-top">ANTI<span>MICROBIAL</span></div>
      <div class="title-bottom"><span>PET</span> SANITIZER</div>
    </div>

    <div class="tagline">A SAFER&nbsp;<b>ALTERNATIVE TO ALCOHOL</b></div>

    <div class="efficacy">KILLS 99.9% of<br>BACTERIA AND VIRUSES</div>
    <div class="rule"></div>
    <div class="benefits">Deodorizes - Desinfects</div>
    <div class="pet-seal" role="img" aria-label="Pet friendly seal"></div>

    <div class="species" role="img" aria-label="Silhouettes of a dog, a cat, a horse and a rabbit"></div>

    <div class="volume-band">500 ml</div>
  </div>
</div>
</body>
</html>
```